Marlow 2400 - KR Layouts
Harold Pinkney
Project: Marlow 2400 - KR Layouts
Creative Brief
Printing
Banks and Credit Unions, Corporate, would appeal to their customers.
1) Each designer should submit 3 different designs under the category "Customer Appreciation." Visit this page to see past designs: http://www.marlow2400.example/exclusive-images/customer-appreciation/. The designs can share comment graphical elements (such as color scheme or layout), but must be different. 2) Please use pixavane.example as your image source (just download the comp image and we will purchase the final image once design is complete). 3) Size = 3.125"w x 7"h 4) No bleeds 5) You can use your own copy or reuse some that are on the http://www.marlow2400.example/exclusive-images/customer-appreciation/.

```html
<!DOCTYPE html>
<html lang="en">
<head>
<meta charset="utf-8">
<title>Customer Appreciation – Card Set</title>
<link href="https://fonts.googleapis.com/css2?family=Great+Vibes&family=Cormorant+Garamond:wght@500&display=swap" rel="stylesheet">
<style>
  :root {
    --backdrop: #d9d6d1;
    --card: #ffffff;
    --ink: #2a2a2a;
    --red: #e8373c;
    --red-deep: #a3161d;
    --red-dark: #8e1218;
    --grey: #a9a9ab;
    --suit-dark: #6f737b;
    --suit-light: #c7c9ce;
    --gold-light: #f6e39a;
    --gold: #c9a236;
    --gold-dark: #8c6a12;
  }
  * { box-sizing: border-box; margin: 0; padding: 0; }
  html, body { width: 1200px; height: 904px; overflow: hidden; }
  body { background: var(--backdrop); position: relative; }

  .card {
    position: absolute;
    top: 98px;
    width: 322px;
    height: 715px;
    background: var(--card);
    box-shadow: 0 3px 10px rgba(0,0,0,.25);
    overflow: hidden;
  }
  .card--heart { left: 49px; }
  .card--crown { left: 438px; }
  .card--trophy { left: 833px; }

  .card__title {
    position: absolute;
    left: 0; right: 0;
    text-align: center;
    color: var(--ink);
    white-space: nowrap;
    line-height: 1;
    transform: translateY(-50%);
  }
  .card__title--script {
    font-family: "Great Vibes", cursive;
    font-size: 31px;
    font-weight: 400;
  }
  .card__title--serif {
    font-family: "Cormorant Garamond", serif;
    font-size: 22px;
    font-weight: 500;
  }
  .card--heart .card__title { top: 290px; }
  .card--crown .card__title { top: 290px; }
  .card--trophy .card__title { top: 302px; }

  .photo { position: absolute; }
  .photo--heart {
    left: 34px; top: 74px; width: 230px; height: 164px;
    background:
      radial-gradient(ellipse 60px 42px at 50% 72%, #e0373d 0%, #c3262c 60%, rgba(195,38,44,0) 100%),
      linear-gradient(90deg, var(--suit-dark), var(--suit-light) 30%, #d9dadd 50%, var(--suit-light) 70%, var(--suit-dark));
  }
  .photo-frame {
    position: absolute;
    left: 38px; top: 70px; width: 232px; height: 164px;
    border: 2px solid var(--red);
    transform: rotate(-5deg);
  }
  .photo--crown {
    left: 56px; top: 51px; width: 209px; height: 209px;
    background: radial-gradient(circle at 50% 45%, #cf3a33, var(--red-deep) 75%);
  }
  .photo--trophy {
    left: 86px; top: 40px; width: 156px; height: 200px;
    background: linear-gradient(180deg, #f4e2a0 0%, #eed88a 30%, #e9e7e2 62%, #f3f3f3 100%);
  }

  .wave { position: absolute; left: 0; bottom: 0; width: 322px; height: 150px; }

  .gold-band {
    position: absolute;
    left: 0; right: 0; top: 670px; height: 15px;
    background: linear-gradient(180deg, var(--gold-light), var(--gold) 45%, var(--gold-dark) 80%, var(--gold-light));
  }
</style>
</head>
<body>

  <article class="card card--heart">
    <div class="photo photo--heart" role="img" aria-label="Photo of a businessman's hands forming a heart around a red heart"></div>
    <div class="photo-frame"></div>
    <h2 class="card__title card__title--script">Customer Appreciation</h2>
    <svg class="wave" viewBox="0 0 322 150" preserveAspectRatio="none">
      <path d="M0 84 C100 112 210 56 322 34 L322 48 C210 70 100 126 0 98 Z" fill="var(--grey)"/>
      <path d="M0 104 C100 130 210 70 322 50 L322 62 C210 84 100 138 0 114 Z" fill="var(--red-deep)"/>
      <path d="M0 116 C100 138 210 80 322 64 L322 150 L0 150 Z" fill="var(--red)"/>
    </svg>
  </article>

  <article class="card card--crown">
    <div class="photo photo--crown" role="img" aria-label="Illustration of a crown made of small icons on a red background"></div>
    <h2 class="card__title card__title--serif">Customer Appreciation</h2>
    <svg class="wave" viewBox="0 0 322 150" preserveAspectRatio="none">
      <path d="M0 100 C120 122 230 80 322 44 L322 150 L0 150 Z" fill="var(--red)"/>
      <path d="M0 106 C120 128 230 88 322 52 L322 150 L0 150 Z" fill="var(--red-dark)"/>
    </svg>
  </article>

  <article class="card card--trophy">
    <div class="photo photo--trophy" role="img" aria-label="Illustration of a white figure holding up a gold trophy"></div>
    <h2 class="card__title card__title--script">Customer Appreciation</h2>
    <div class="gold-band"></div>
  </article>

</body>
</html>
```